Web Design Project

We need a website design for our marketing agency: loftwaveo.com.au

We want something that is eye-catching and will wow audiences, yet at the same time it cannot turn-off corporate clients. The website should be highly focused on conversions with numerous call to actions on each page.

We like blue as our primary colour and have a mascot (the spider on the current website)

Target Market(s)

small business owners
small corporations
enterprise level business clients

Industry/Entity Type

Marketing

Requirements
Must have
• must incorporate the agency mascot (the spider on the website)

```html
<!DOCTYPE html>
<html lang="en">
<head>
<meta charset="utf-8">
<title>Loftwaveo – High ROI Digital Marketing</title>
<link rel="stylesheet" href="https://fonts.googleapis.com/css2?family=Philosopher:wght@400;700&family=Arimo:wght@400;700&display=swap">
<style>
:root{
  --sky-top:#7fc4ee;
  --sky-mid:#bfe3f8;
  --sky-low:#e6f4fc;
  --page:#d9effb;
  --ink:#0d5f92;
  --ink-strong:#0a4d7c;
  --text-blue:#1478b8;
  --tile:#a9d8f4;
  --tile-edge:#d7effc;
  --nav:#111214;
  --btn:#8fc7ea;
  --field:#e8f5fd;
  --footer:#1a2630;
  --footer-text:#8ea3b3;
  --footer-line:#4a5c6a;
  --white:#ffffff;
}
*{box-sizing:border-box;margin:0;padding:0}
html,body{width:905px;height:1200px;overflow:hidden}
body{position:relative;background:var(--page);font-family:"Arimo",Arial,sans-serif;color:var(--text-blue)}
.abs{position:absolute}

/* header */
.hero{left:0;top:0;width:905px;height:390px;
  background:linear-gradient(180deg,var(--sky-top) 0%,var(--sky-mid) 55%,var(--sky-low) 100%);
  border-bottom:2px solid var(--white)}
.brand{left:59px;top:26px;font-family:"Philosopher",sans-serif;font-weight:700;font-size:30px;color:#5d8fd8;letter-spacing:1px}
.main-nav{left:193px;top:64px;width:527px;height:32px;background:var(--nav);border-radius:5px;display:flex;align-items:center;padding-left:7px}
.main-nav a{font-weight:700;font-size:11px;color:var(--white);text-decoration:none;text-transform:uppercase;height:24px;line-height:24px;padding:0 13px;white-space:nowrap}
.main-nav a.is-current{background:linear-gradient(180deg,#fff,#bfc4c8);color:#fff;text-shadow:0 0 2px #777;border-radius:3px;padding:0 22px;margin-right:6px}
.call-box{left:708px;top:21px;width:184px;height:38px;background:var(--white);border:1px solid #c9d4dc;border-radius:6px;box-shadow:0 1px 3px rgba(0,0,0,.2)}
.call-label{position:absolute;left:0;top:0;width:17px;height:100%;border-right:1px solid #ccd;font-size:7px;color:#557;writing-mode:vertical-rl;transform:rotate(180deg);text-align:center}
.call-number{position:absolute;left:30px;top:4px;width:150px;text-align:center;font-size:13px;color:#333}
.call-hours{position:absolute;left:30px;top:22px;width:150px;text-align:center;font-size:8px;color:#555}
.art-laptop{left:33px;top:162px;width:294px;height:205px;border-radius:10px;
  background:linear-gradient(160deg,rgba(255,255,255,.55) 0%,#d6f0a8 30%,#a8dc63 58%,#6fbd3a 100%);
  border:1px solid rgba(255,255,255,.8);box-shadow:0 6px 14px rgba(60,120,160,.25)}
.art-mascot{left:540px;top:113px;width:200px;height:272px;border-radius:10px;
  background:linear-gradient(170deg,rgba(255,255,255,.6) 0%,#d8dde2 30%,#a7b0b8 65%,#7d878f 100%);
  border:1px solid rgba(255,255,255,.8);box-shadow:0 6px 14px rgba(60,120,160,.25)}
.tagline{left:704px;top:349px;white-space:nowrap;font-family:"Philosopher",sans-serif;font-weight:700;font-size:16px;color:#3a7fcf;letter-spacing:.3px}

/* headings */
.sec-title{font-family:"Philosopher",sans-serif;font-size:14px;font-weight:400;color:var(--ink-strong);white-space:nowrap}
.sec-title.barred{padding-left:6px;border-left:4px solid #5b9fd2;line-height:16px}
.body-copy{font-size:8.5px;line-height:14.5px;color:var(--text-blue)}
.more{display:inline-block;background:var(--btn);color:var(--white);font-size:6px;font-weight:700;padding:1px 4px;border:1px solid #d5edfb}

/* welcome */
.welcome{left:92px;top:447px;width:190px}
.welcome .body-copy{margin-top:6px;font-size:8px;line-height:14.5px}
.feature-tile{top:455px;width:156px;height:101px;background:linear-gradient(180deg,var(--tile-edge),var(--tile));border:1px solid var(--white)}
.feature-tile .art{position:absolute;left:30px;top:6px;width:96px;height:88px;border-radius:50%;background:radial-gradient(circle,#4aa3d6 0%,rgba(169,216,244,0) 70%)}
.feature-caption{top:569px;width:156px;text-align:center;font-family:"Philosopher",sans-serif;font-size:12px;color:var(--ink-strong);white-space:nowrap}

.rule{left:90px;width:715px;height:1px;background:linear-gradient(90deg,rgba(122,180,220,0),#7ab4dc 20%,#7ab4dc 80%,rgba(122,180,220,0))}

/* services */
.service{width:210px}
.service-head{display:flex;align-items:center;gap:4px;height:18px;margin-left:-9px}
.service-icon{width:26px;height:18px;flex:none}
.service .sec-title{font-size:13px}
.service .body-copy{margin-top:6px}
.service .more{margin-top:2px}

/* testimonial & comment */
.panel{top:901px;width:331px;height:175px;background:rgba(255,255,255,.55);border:6px solid rgba(255,255,255,.7)}
.quote{position:absolute;left:8px;width:306px;height:66px;border-bottom:1px solid #a8d2ee}
.avatar{position:absolute;left:6px;top:2px;width:58px;height:58px;background:var(--tile);border:3px solid #e6f4fc}
.quote p{position:absolute;left:86px;font-size:8.5px;font-weight:700;color:var(--ink);white-space:nowrap}
.quote .mark{position:absolute;font-size:16px;font-family:Georgia,serif;color:var(--ink)}
.panel-btn{position:absolute;font-size:7px;font-weight:700;color:var(--white);background:var(--btn);border:1px solid #e4f4fd;padding:2px 6px}
.field{position:absolute;left:16px;width:79px;height:14px;background:var(--field);font-size:7px;color:#6ba3cb;line-height:14px;padding-left:6px}
.message{position:absolute;left:110px;width:192px;height:76px;background:var(--field)}

/* footer */
.footer{left:0;top:1101px;width:905px;height:99px;background:var(--footer);border-top:2px solid #3b4c5a}
.footer-brand{left:22px;font-family:"Philosopher",sans-serif;font-weight:700;font-size:34px;color:#6f9ee0}
.footer-address{left:190px;font-size:6px;line-height:18px;color:var(--footer-text);width:200px}
.footer-col{font-size:7.5px;line-height:10px;color:var(--footer-text);padding-left:12px;border-left:1px solid var(--footer-line);height:76px;white-space:nowrap}
.footer-col .head{margin-bottom:10px}
.social{display:flex;gap:5px}
.social span{width:15px;height:15px;border-radius:2px}
</style>
</head>
<body>

<header class="abs hero"></header>
<div class="abs brand">Loftwaveo</div>
<nav class="abs main-nav">
  <a class="is-current" href="#">Home</a><a href="#">Service</a><a href="#">Blog</a><a href="#">SEO Pricing</a><a href="#">SEM</a><a href="#">About</a><a href="#">Contact</a>
</nav>
<div class="abs call-box">
  <span class="call-label">Call now</span>
  <span class="call-number">(+617) 3000 4812</span>
  <span class="call-hours">AM 10:00 – PM 6:00</span>
</div>
<div class="abs art-laptop" role="img" aria-label="Illustration of an open laptop with a white dove, music notes and leaves flying out"></div>
<div class="abs art-mascot" role="img" aria-label="Illustration of the agency mascot, a silver robotic spider"></div>
<div class="abs tagline">High ROI Digital Marketing</div>

<section class="abs welcome">
  <h2 class="sec-title">Welcome</h2>
  <p class="body-copy">Welcome to Loftwaveo. More text here More text here More text here More text here More text here More text here More text here.</p>
</section>

<div class="abs feature-tile" style="left:311px"><div class="art" role="img" aria-label="Glossy blue at-sign graphic"></div></div>
<div class="abs feature-tile" style="left:481px"><div class="art" role="img" aria-label="Blue ribbon arrow graphic"></div></div>
<div class="abs feature-tile" style="left:651px"><div class="art" role="img" aria-label="Magnifying glass graphic"></div></div>
<div class="abs feature-caption" style="left:297px;width:184px">Online Ad Management</div>
<div class="abs feature-caption" style="left:481px">SEO Packages</div>
<div class="abs feature-caption" style="left:651px">Social Media</div>

<div class="abs rule" style="top:597px"></div>
<div class="abs rule" style="top:614px"></div>

<svg width="0" height="0" style="position:absolute">
  <symbol id="icon-arrow" viewBox="0 0 26 18"><circle cx="13" cy="9" r="7" fill="none" stroke="#5b9fd2" stroke-width="2"/><path d="M1 9h14m-4-4 4 4-4 4" fill="none" stroke="#2f7fbf" stroke-width="2"/></symbol>
  <symbol id="icon-search" viewBox="0 0 26 18"><circle cx="10" cy="8" r="5" fill="none" stroke="#5b9fd2" stroke-width="2"/><path d="M14 12l5 5" stroke="#2f7fbf" stroke-width="2"/></symbol>
</svg>

<article class="abs service" style="left:92px;top:629px">
  <div class="service-head"><svg class="service-icon"><use href="#icon-arrow"/></svg><h3 class="sec-title barred">Loftwaveo Digital Marketing</h3></div>
  <p class="body-copy">Online marketing channels are a major factor almost any business. Loftwaveo is a digital marketing agency focused on results and ROI.</p>
  <span class="more">MORE</span>
</article>
<article class="abs service" style="left:359px;top:629px">
  <div class="service-head"><svg class="service-icon"><use href="#icon-arrow"/></svg><h3 class="sec-title barred">SEO Services</h3></div>
  <p class="body-copy">It's not just about quantity of traffic but quality. Loftwaveo's SEO services can drive targeted traffic to your site maximizing your visibility and increasing revenue.</p>
  <span class="more">MORE</span>
</article>
<article class="abs service" style="left:616px;top:629px;width:215px">
  <div class="service-head"><svg class="service-icon"><use href="#icon-arrow"/></svg><h3 class="sec-title barred">SEM Services</h3></div>
  <p class="body-copy">High ROI online advertising is a specialty of ours. Effectively managing search engine marketing campaigns takes a lot of time, experience and expertise.</p>
  <span class="more">MORE</span>
</article>
<article class="abs service" style="left:92px;top:742px">
  <div class="service-head"><svg class="service-icon"><use href="#icon-search"/></svg><h3 class="sec-title barred">Search Engine Optimisation</h3></div>
  <p class="body-copy">A website without traffic is useless. Traffic is the commodity of the internet: driving information &amp; business in our online economy.</p>
  <span class="more">MORE</span>
</article>
<article class="abs service" style="left:359px;top:742px">
  <div class="service-head"><svg class="service-icon"><use href="#icon-arrow"/></svg><h3 class="sec-title barred">SEO Brisbane</h3></div>
  <p class="body-copy">Need Brisbane SEO services? We can help! Loftwaveo is located in Brisbane, Australia and service clients Australia wide &amp; overseas.</p>
  <span class="more">MORE</span>
</article>

<div class="abs rule" style="top:843px"></div>

<h2 class="abs sec-title barred" style="left:97px;top:868px">Testimonial</h2>
<h2 class="abs sec-title barred" style="left:471px;top:868px">Leave a Comment</h2>

<section class="abs panel" style="left:100px">
  <div class="quote" style="top:6px">
    <div class="avatar" role="img" aria-label="Client avatar placeholder"></div>
    <span class="mark" style="left:98px;top:4px">“</span>
    <p style="top:17px;left:110px">I am very much happy with the service.</p>
    <p style="top:41px">Loftwaveo is very good in it's business.</p>
    <span class="mark" style="left:264px;top:30px">”</span>
  </div>
  <div class="quote" style="top:78px;border-bottom:none">
    <div class="avatar" role="img" aria-label="Client avatar placeholder"></div>
    <span class="mark" style="left:98px;top:4px">“</span>
    <p style="top:17px;left:110px">I am very much happy with the service.</p>
    <p style="top:41px">Loftwaveo is very good in it's business.</p>
    <span class="mark" style="left:264px;top:30px">”</span>
  </div>
  <span class="panel-btn" style="right:6px;bottom:4px">MORE</span>
</section>

<section class="abs panel" style="left:476px">
  <span class="field" style="top:70px">Name</span>
  <span class="field" style="top:91px">E-Mail</span>
  <span class="field" style="top:112px">Phone</span>
  <span class="field" style="top:133px">Website</span>
  <div class="message" style="top:70px"></div>
  <span class="panel-btn" style="right:12px;bottom:4px">SEND</span>
</section>

<footer class="abs footer"></footer>
<div class="abs footer-brand" style="top:1118px">Loftwaveo</div>
<div class="abs footer-address" style="top:1122px">Level 12, Harbour House 40 Quay Lane Brisbane, QLD, 4000<br>Copyright (c) 2011 LoftwaveoINC. All Rights Reserved.</div>
<div class="abs footer-col" style="left:401px;top:1114px">Home<br>Service<br>Blog<br>SEO Pricing<br>SEM<br>About<br>Contact</div>
<div class="abs footer-col" style="left:477px;top:1114px"><div class="head">Services</div>Online Ad Management<br>SEO Packages<br>Social Media</div>
<div class="abs footer-col" style="left:583px;top:1114px;padding-top:20px">Loftwaveo Digital Marketing<br>Search Engine Optimisation<br>SEO Services<br>SEO Brisbane<br>SEM Services</div>
<div class="abs social" style="left:726px;top:1110px">
  <span style="background:#3b5998"></span><span style="background:#3fa9e0"></span><span style="background:#2a7ab3"></span><span style="background:#e8892b"></span>
</div>

</body>
</html>
```